Stanbrook Fire Services Pty Ltd

We need business cards for a company based in Perth, we install, service and maintain fire equipment.
On the front we want a great design with our logo and a small spot for our full company name, general company email address and office number. On the back we need space for our name, title, mobile number and email address on the back.

Target Market(s)

Facility managers and commercial/industrial building owners/occupiers.

Contact Information for Business Card

Font styles to use
Sans Serif

Requirements
Must have
• Please only submit 5 of your best samples.
Darker tones are preferred.
Nice to have
• We want to use, black, red and grey. Keep it modern and clean.
I've attached the company logo and a sample of a boarder we use on our emergency plans.
Should not have
• No preference. Let the designer choose.

```html
<!DOCTYPE html>
<html lang="en">
<head>
<meta charset="utf-8">
<title>Stanbrook Fire Services – Business Cards</title>
<link href="https://fonts.googleapis.com/css2?family=Montserrat:wght@400;500;600;800&display=swap" rel="stylesheet">
<style>
  :root {
    --page-bg: #5d5e62;
    --card-black: #0d0d0e;
    --card-edge: #1a1a1c;
    --brand-red: #ee1c25;
    --emboss-grey: #2a2a2c;
    --muted-blue: #4a5566;
    --text-white: #f2f2f2;
  }
  * { margin: 0; padding: 0; box-sizing: border-box; }
  html, body {
    width: 1200px; height: 1200px; overflow: hidden;
    background: var(--page-bg);
    font-family: "Montserrat", sans-serif;
  }
  .canvas {
    position: relative; width: 1200px; height: 1200px;
    display: flex; flex-direction: column; align-items: center; justify-content: center; gap: 44px;
  }
  .card {
    position: relative; width: 900px; height: 514px;
    border-radius: 28px;
    background: radial-gradient(circle at 40% 35%, var(--card-edge), var(--card-black) 70%);
    box-shadow: 0 18px 40px rgba(0,0,0,.45);
    overflow: hidden;
  }

  /* Front */
  .front-brand {
    position: absolute; left: 0; right: 0; top: 150px;
    display: flex; align-items: center; justify-content: center; gap: 18px;
  }
  .front-brand .brand-square { width: 34px; height: 34px; background: var(--emboss-grey); }
  .front-brand .brand-name {
    font-weight: 800; font-size: 84px; letter-spacing: 2px; color: var(--emboss-grey);
  }
  .front-details {
    position: absolute; left: 0; right: 0; top: 372px; text-align: center; color: var(--muted-blue);
    font-size: 19px; line-height: 1.55;
  }
  .front-details .company-line::before,
  .front-details .company-line::after {
    content: ""; display: inline-block; width: 7px; height: 7px; border-radius: 50%;
    background: var(--brand-red); vertical-align: middle; margin: 0 10px 4px;
  }

  /* Back */
  .person {
    position: absolute; left: 60px; top: 200px;
  }
  .person-name {
    color: var(--brand-red); font-weight: 600; font-size: 30px; letter-spacing: 5px; text-transform: uppercase;
  }
  .person-title {
    color: var(--text-white); font-weight: 400; font-size: 17px; letter-spacing: 4px; text-transform: uppercase; margin-top: 4px;
  }
  .divider {
    position: absolute; left: 280px; right: 70px; top: 290px; height: 2px; background: var(--brand-red);
  }
  .back-brand {
    position: absolute; right: 70px; top: 110px; display: flex; align-items: center; gap: 14px;
  }
  .back-brand .brand-square { width: 26px; height: 26px; background: var(--brand-red); }
  .back-brand .brand-name { color: var(--brand-red); font-weight: 800; font-size: 54px; letter-spacing: 1px; }
  .contact-list {
    position: absolute; right: 70px; top: 330px; list-style: none;
    color: var(--text-white); font-size: 21px; letter-spacing: 2px;
  }
  .contact-list li { display: flex; align-items: center; gap: 18px; margin-bottom: 10px; }
  .contact-list svg { width: 20px; height: 20px; flex: none; }
</style>
</head>
<body>
<main class="canvas">

  <section class="card card-front" aria-label="Card front">
    <div class="front-brand">
      <span class="brand-square"></span>
      <span class="brand-name">STANBROOK</span>
    </div>
    <div class="front-details">
      <p class="company-line">Stanbrook Fire Services Pty Ltd</p>
      <p class="office-line">08 5550 1234 | info@stanbrookfire.com.au</p>
    </div>
  </section>

  <section class="card card-back" aria-label="Card back">
    <div class="back-brand">
      <span class="brand-square"></span>
      <span class="brand-name">STANBROOK</span>
    </div>
    <div class="person">
      <p class="person-name">Marcus Hale</p>
      <p class="person-title">Founder &amp; CEO</p>
    </div>
    <div class="divider"></div>
    <ul class="contact-list">
      <li>
        <svg viewBox="0 0 24 24" fill="var(--brand-red)"><path d="M6.6 10.8a15.1 15.1 0 0 0 6.6 6.6l2.2-2.2a1 1 0 0 1 1-.25 11.4 11.4 0 0 0 3.6.57 1 1 0 0 1 1 1V20a1 1 0 0 1-1 1A17 17 0 0 1 3 4a1 1 0 0 1 1-1h3.5a1 1 0 0 1 1 1c0 1.25.2 2.45.57 3.57a1 1 0 0 1-.25 1z"/></svg>
        +61 400 555 017
      </li>
      <li>
        <svg viewBox="0 0 24 24" fill="none" stroke="var(--brand-red)" stroke-width="2"><rect x="3" y="5" width="18" height="14" rx="1"/><path d="M3 6l9 7 9-7"/></svg>
        ceo@stanbrookfire.com.au
      </li>
      <li>
        <svg viewBox="0 0 24 24" fill="none" stroke="var(--brand-red)" stroke-width="2"><circle cx="12" cy="12" r="9"/><path d="M3 12h18M12 3c3 3 3 15 0 18M12 3c-3 3-3 15 0 18"/></svg>
        www.stanbrookfire.com.au
      </li>
    </ul>
  </section>

</main>
</body>
</html>
```